Property Management Company looking for a high-end business card, letterhead and envelope design.

We provide high-end / boutique property management for real estate investors or individuals looking for someone to manage their portfolio. we are looking for a cohesive high-end design for our business cards, letterhead and envelopes.

Target Market(s)

Real Estate Investors

Industry/Entity Type

Real Estate

Requirements
Must have
• business card, letterhead and envelope design - logo attached

```html
<!DOCTYPE html>
<html lang="en">
<head>
<meta charset="utf-8">
<title>Harborline Property Management – Business Card</title>
<link rel="stylesheet" href="https://fonts.googleapis.com/css2?family=Montserrat:wght@500;600;700&family=Roboto:wght@400;500&display=swap">
<style>
  :root {
    --brand-blue: #0d4f8b;
    --deep-blue: #0b4a84;
    --slate-grey: #a9a9ab;
    --ink: #3a3a3c;
    --paper: #ffffff;
    --backdrop: #d9d9d7;
  }
  * { box-sizing: border-box; margin: 0; padding: 0; }
  html, body { width: 1200px; height: 801px; overflow: hidden; }
  body {
    background: var(--backdrop);
    position: relative;
    font-family: "Roboto", sans-serif;
  }
  .card {
    position: absolute;
    top: 246px;
    width: 540px;
    height: 309px;
    overflow: hidden;
    box-shadow: 0 6px 18px rgba(0,0,0,0.18);
  }
  .card--front { left: 40px; background: var(--paper); }
  .card--back  { left: 620px; background: var(--deep-blue); }

  .wordmark {
    position: absolute;
    left: 38px;
    top: 112px;
    color: var(--brand-blue);
  }
  .wordmark__name {
    font-family: "Montserrat", sans-serif;
    font-weight: 600;
    font-size: 29px;
    letter-spacing: 4px;
    line-height: 1;
  }
  .wordmark__tagline {
    font-family: "Montserrat", sans-serif;
    font-weight: 500;
    font-size: 10.5px;
    letter-spacing: 3.6px;
    margin-top: 8px;
  }

  .divider {
    position: absolute;
    left: 292px;
    top: 72px;
    width: 1.5px;
    height: 126px;
    background: var(--brand-blue);
  }

  .contact-block {
    position: absolute;
    left: 312px;
    top: 64px;
  }
  .contact-block__name {
    font-family: "Montserrat", sans-serif;
    font-weight: 700;
    font-size: 17px;
    color: var(--brand-blue);
    letter-spacing: 0.3px;
  }
  .contact-block__title {
    font-family: "Montserrat", sans-serif;
    font-weight: 600;
    font-size: 13.5px;
    color: var(--ink);
    margin-top: 2px;
  }
  .contact-list { list-style: none; margin-top: 14px; }
  .contact-list li {
    display: flex;
    align-items: center;
    gap: 8px;
    font-size: 13.5px;
    color: var(--ink);
    line-height: 20px;
  }
  .contact-list svg { width: 13px; height: 13px; fill: var(--brand-blue); flex: none; }

  .address-band {
    position: absolute;
    left: 110px;
    top: 238px;
    width: 370px;
    height: 28px;
    background: var(--brand-blue);
    clip-path: polygon(0 0, 100% 0, 94% 100%, 0 100%);
    display: flex;
    align-items: center;
    gap: 7px;
    padding-left: 16px;
    color: var(--paper);
    font-size: 13.5px;
    letter-spacing: 0.2px;
  }
  .address-band svg { width: 11px; height: 14px; fill: var(--paper); }
  .corner-tab {
    position: absolute;
    left: 470px;
    top: 238px;
    width: 70px;
    height: 28px;
    background: var(--slate-grey);
    clip-path: polygon(22% 0, 100% 0, 100% 100%, 0 100%);
  }

  .back-name {
    position: absolute;
    inset: 0;
    display: flex;
    align-items: center;
    justify-content: center;
    gap: 12px;
    font-family: "Montserrat", sans-serif;
    font-weight: 600;
    font-size: 26px;
    letter-spacing: 4px;
    color: var(--paper);
  }
  .back-name__square { width: 14px; height: 14px; background: var(--paper); }
</style>
</head>
<body>

<section class="card card--front" aria-label="Business card front">
  <div class="wordmark">
    <div class="wordmark__name">HARBORLINE</div>
    <div class="wordmark__tagline">PROPERTY MANAGEMENT</div>
  </div>

  <div class="divider"></div>

  <div class="contact-block">
    <div class="contact-block__name">MARCUS ELLERY</div>
    <div class="contact-block__title">Managing Director</div>
    <ul class="contact-list">
      <li>
        <svg viewBox="0 0 16 16" aria-hidden="true"><path d="M3.6 1.2l2.3 2.6-1.2 1.8c.9 2 2.6 3.7 4.6 4.6l1.8-1.2 2.6 2.3-1.2 2.3C7.6 13.9 2.1 8.4 1.3 3.5z"/></svg>
        555.014.2207
      </li>
      <li>
        <svg viewBox="0 0 16 16" aria-hidden="true"><path d="M4 1h7v4H4zM1 6h14v7h-3v2H4v-2H1zm4 4v4h6v-4z"/></svg>
        555.014.3380
      </li>
      <li>
        <svg viewBox="0 0 16 16" aria-hidden="true"><path d="M1 3h14v10H1zm1.5 1.2V5l5.5 4 5.5-4v-.8z"/></svg>
        hello@harborlinepm.com
      </li>
      <li>
        <svg viewBox="0 0 16 16" aria-hidden="true"><circle cx="8" cy="8" r="7"/></svg>
        www.harborlinepm.com
      </li>
    </ul>
  </div>

  <div class="address-band">
    <svg viewBox="0 0 12 16" aria-hidden="true"><path d="M6 0a6 6 0 0 1 6 6c0 4-6 10-6 10S0 10 0 6a6 6 0 0 1 6-6zm0 3.5a2.5 2.5 0 1 0 0 5 2.5 2.5 0 0 0 0-5z"/></svg>
    48 Linden Court, Maple Ridge, ON L2K 4P7
  </div>
  <div class="corner-tab"></div>
</section>

<section class="card card--back" aria-label="Business card back">
  <div class="back-name">
    <span class="back-name__square"></span>
    HARBORLINE
  </div>
</section>

</body>
</html>
```